Plakat-Design für IT-Systemhaus
orvo IT Solutions
The winner of our first design contests on this site. Can only say positive things about them. They work fast, respond in a timely manner and created a great design for us. Overall we're very happy with Tindrel.
Zielgruppe
Wir sind ein IT-Systemhaus mit dem Fokus auf individuelle Cloud Lösungen inkl. bester Kundenbetreuung.
Unsere primäre Zielgruppe sind Unterhnemenskunden, sprich das B2B Geschäft.
Aus der Gruppe der Unternehmenskunden interessieren uns besonders kleine und mittelständische Unternehmen.
Unser Corporate Design ist modern und dennoch auffällig gehalten.
Unsere bevorzugt Schriftart ist 'Ubuntu' bzw. 'Ubuntu Light'.
Unsere Grundfarben sind Orange (#ff8303) Grau (#747474).
Als orientierungshilfe haben wir unser Vorlage für Blöcke und Flyer mit angehangen.
Aufgabenstellung
Es handelt sich um eine Geländerwerbung (doppelseitig) zwischen einer Tankstelle und einer Straße gelegen. (Siehe Anhang)
Die Maße des Anzeitgetafel sind wie folgt: Querformat 135 x 65 (breite x höhe)
Gerne würden wir auf eine etwas provokantere Fragestellung zurückgreifen, um Aufmerksamkeit zu eregen.
Gleichzeitig möchten wir als Lösungsfinder der Fragestellung wargenommen werden.
Gut gefallen hat uns diese Lösung: https://www.grafikbrett.at/527190-plakat-fuer-it-systemhaus
Des Weiteren sollte die Anzeige unser Logo, Webadresse sowie unsere Telefonnummer enthalten.
Für Kreative Vorschläge sind wir dankbar.

```html
<!DOCTYPE html>
<html lang="de">
<head>
<meta charset="utf-8">
<title>orvo IT Solutions – Plakat</title>
<link href="https://fonts.googleapis.com/css2?family=Ubuntu:wght@400;500;700&display=swap" rel="stylesheet">
<style>
  :root {
    --page-bg: #e9e9e9;
    --orange: #d9822b;
    --grey: #8c8c8c;
    --white: #ffffff;
    --sky-top: #2a5a9e;
    --sky-mid: #3f8ad0;
    --cloud: #e6edf5;
  }
  html, body {
    margin: 0;
    width: 1200px;
    height: 848px;
    overflow: hidden;
    background: var(--page-bg);
    font-family: 'Ubuntu', sans-serif;
  }
  .poster {
    position: absolute;
    left: 30px;
    top: 147px;
    width: 1140px;
    height: 553px;
    background: var(--white);
    overflow: hidden;
  }
  .sky-photo {
    position: absolute;
    left: 0;
    top: 0;
    width: 1140px;
    height: 368px;
    background: linear-gradient(180deg, var(--sky-top) 0%, var(--sky-mid) 38%, #a9c6e3 58%, var(--cloud) 78%, #f2f5f9 100%);
  }
  .accent-rule {
    position: absolute;
    left: 0;
    top: 368px;
    width: 1140px;
    height: 8px;
    background: var(--orange);
  }
  .headline {
    position: absolute;
    left: 70px;
    margin: 0;
    font-weight: 500;
    font-size: 65px;
    line-height: 68px;
    color: var(--white);
    text-shadow: 2px 3px 6px rgba(0, 0, 0, 0.45);
    white-space: nowrap;
  }
  .headline--question { top: 95px; }
  .headline--answer { top: 190px; }
  .web-tag {
    position: absolute;
    left: 785px;
    top: 32px;
    width: 420px;
    height: 96px;
    background: var(--orange);
    border-radius: 48px 0 0 48px;
    transform: rotate(-8deg);
    transform-origin: left center;
    box-sizing: border-box;
    padding-left: 52px;
    display: flex;
    align-items: center;
    color: var(--white);
    font-weight: 500;
    font-size: 50px;
  }
  .claim {
    position: absolute;
    left: 70px;
    top: 405px;
    margin: 0;
    font-weight: 500;
    font-size: 33px;
    line-height: 37px;
    color: var(--grey);
  }
  .brand-name {
    position: absolute;
    left: 840px;
    top: 405px;
    width: 260px;
    margin: 0;
    font-weight: 400;
    color: var(--orange);
    text-align: center;
  }
  .brand-name .brand-word {
    display: block;
    font-size: 84px;
    line-height: 84px;
  }
  .brand-name .brand-sub {
    display: block;
    font-size: 28px;
    line-height: 34px;
  }
</style>
</head>
<body>
  <main class="poster">
    <div class="sky-photo" role="img" aria-label="Foto: blauer Himmel über einer weißen Wolkendecke"></div>
    <div class="accent-rule"></div>

    <h1 class="headline headline--question">Über den Wolken …?</h1>
    <p class="headline headline--answer">Wir fühlen uns auch innerhalb<br>der Clouds ganz wohl.</p>

    <div class="web-tag">orvo-it.de/</div>

    <p class="claim">Individuelle Cloud-Lösungen inkl.<br>bester Kundenbetreuung für Ihr<br>Unternehmen.</p>

    <p class="brand-name"><span class="brand-word">orvo</span><span class="brand-sub">IT Solutions</span></p>
  </main>
</body>
</html>
```